Velvet Larks website

Home page and info page design needed
PRODUCTION NOTES

* 10 Page Website
* Blog

CLIENT PURPOSE

• Provide information not easily/commonly available for women over 40
• Focus on unusual opportunities
• Fun / Informative / Unique / Helpful

PLATFORM
Wordpress

SERVICES
Inform / Encourage / Emphasise - Information / Topics etc -
Promote products for the over 40’s - From advertisers etc. -
- -

COMPETITION
Cycle Compass - cyclecompass.co.uk
Kinfolk Hub - kinfolkhub.com
Stay Spry Past Sixty - stayspryspastsixty.com

WEBSITE(S) CLIENT LIKES
kinfolkhub.com
ladytinkerstyle.com
qvn.co.uk
tallowbrook.org.uk

WEBSITE CLIENT DOES NOT LIKE
cyclecompass.co.uk

COMPANY LOGO
Customer has a company logo - their existing site is here http://velvetlarks.com - this is the logo you should use , you need to reflect the feel of the logo throughout the whole design

COLOURS:
as the logo

STRAPLINE:
Dangerously Fascinating Women

EMAIL ADDRESSES TO APPEAR ON WEBSITE:
info@velvetlarks.com -

WEBSITE THEME:
Womens Health

IMAGES THAT BEST REFLECT YOUR COMPANY: •
Retro / Funky / Unusual / Eye-catching• As per original site but more sophisticated•
Focus groups said they liked style/look of old site but thought it looked a bit ‘young’ for target group

HEADER IMAGE:
Women - Active

PAGES:
Home
About Us
Explore Something New
Health & Well Being –
Relationships
Blog
Mind, Body & Soul
Contact

MESSAGE BANNERS:

Need to show recent Blog entries.-Maybe have TOP 5 related issues?
* Boost your sex drive.
* What is HRT? * Suffering from migraines?
* Treatment Options
* Do symptoms get worse when you start on HRT?-Picture of Fenella & Morwen‘ Written by like minded women’
Link to blog entry about the founders of the website?-Maybe a Product option?Advertising option...-Your story..

USER JOURNEYS:

General Service > Land on website > Service Banners > Info Pages > Contact FormQuestions > Land on website > Message Banners > Info Pages > Contact FormContact > Land on website > Clear Telephone / Email Banner > Contact Form

CALL TO ACTION BANNER:

Search the blog..

-

KEYWORDS THAT RELATE TO YOUR BUSINESS:

Menopause
Hormones
Mid Life
Stress
Empty Nest
Womans Health
HRT
Body & Soul
hormone replacement therapy

LOCATION(S):

United Kingdom -

here is the link to the clients current site
http://velvetlarks.com/index.html

Target Market(s)

woman over 40+

Industry/Entity Type

Consulting

Number of Pages Required

1 page

Requirements
Must have
• take the colours and style of the logo and use throughout the design
Should not have
• Cliche pictures of older woman - you need to give the right balance of seriousness and fun - must not come accross as boring BUT also not too light hearted

```html
<!DOCTYPE html>
<html lang="en">
<head>
<meta charset="utf-8">
<title>Velvet Larks – Home</title>
<link href="https://fonts.googleapis.com/css2?family=Arimo:wght@400;700&family=Cinzel:wght@400;700&family=Lora:ital@1&display=swap" rel="stylesheet">
<style>
:root{
  --page:#f2e1c4;
  --orange:#f7a81b;
  --orange-deep:#e8781e;
  --red:#c8321c;
  --gold:#d9a33a;
  --cream:#fff8ee;
  --pale:#fff1d6;
  --link-blue:#2aa0d8;
  --ink:#222;
  --grey:#b5b5b5;
  --line:#e8c98a;
  --white:#fff;
  --magenta:#d1147a;
}
*{box-sizing:border-box;margin:0;padding:0}
html,body{width:900px;height:1200px;overflow:hidden}
body{background:var(--page);font-family:"Arimo",Arial,sans-serif;color:var(--ink);position:relative}
.abs{position:absolute}
.banner{position:absolute;background:var(--white);border:1px solid var(--grey);color:var(--grey);font-size:11px;display:flex;align-items:center;justify-content:center;letter-spacing:.3px}

/* header */
.masthead{left:88px;top:67px;width:723px;height:140px;border-radius:8px 8px 0 0;overflow:hidden;
  background:linear-gradient(90deg,#4fa6dc 0%,#a9d6f0 22%,#e8f2f6 40%,#fde2ab 62%,#fbb445 85%,#f8a122 100%)}
.masthead-photo{left:215px;top:0;width:200px;height:133px;background:linear-gradient(180deg,#f3d3a8 0%,#eec08a 60%,#f6e3c4 100%)}
.brand{left:22px;top:44px;display:flex;align-items:center;gap:6px;font-family:"Cinzel",serif;font-weight:700;font-size:22px;color:var(--orange-deep)}
.brand i{display:block;width:20px;height:20px;border-radius:50%;background:var(--orange-deep)}
.tagline{left:52px;top:74px;font-family:"Lora",serif;font-style:italic;font-size:9px;color:var(--orange-deep)}
.strapline{left:467px;top:22px;width:240px;font-family:"Lora",serif;font-style:italic;font-size:14.5px;line-height:16.5px;color:var(--orange-deep)}

/* nav */
.topnav{left:88px;top:200px;width:723px;height:26px;background:var(--white);border-radius:14px 14px 0 0;font-size:8.5px}
.topnav a{position:absolute;top:9px;text-decoration:none;color:#888}
.topnav .home-tab{left:0;top:0;width:56px;height:26px;background:var(--white);border-right:2px solid #eee;border-radius:12px 12px 0 0}
.topnav .current{color:var(--orange-deep)}
.topnav .contact{color:var(--link-blue)}
.topnav .search-label{color:var(--orange-deep)}
.search-box{position:absolute;left:522px;top:6px;width:100px;height:15px;border:1px solid var(--orange);border-radius:8px;background:#f3f9fd}
.rss{position:absolute;left:698px;top:4px;width:19px;height:19px}

.tabs{left:88px;top:226px;width:723px;height:50px;background:var(--white)}
.tab{position:absolute;top:2px;height:44px;width:141px;border:1px solid #f5c77a;border-radius:0 0 18px 0;
  background:linear-gradient(180deg,#fff6e6,#fde7bd);display:flex;align-items:center;justify-content:center;text-align:center;
  font-family:"Cinzel",serif;font-size:8.5px;line-height:10px;color:var(--orange-deep)}
.tab.active{background:linear-gradient(180deg,#fde7b5,#fbbf5c);color:var(--red);font-size:10.5px;justify-content:flex-start;padding-left:25px}
.tab.active svg{position:absolute;right:6px;top:11px}

/* main */
.main{left:88px;top:276px;width:723px;height:784px;background:var(--white)}
.content{left:93px;top:280px;width:427px;height:773px;background:var(--cream);border:1px solid #f5ead8}
.article{position:absolute;left:59px;width:355px}
.article h2{font-family:"Cinzel",serif;font-weight:400;font-size:11px;color:var(--orange-deep);padding:0 0 2px 34px;border-bottom:1px solid var(--line);letter-spacing:.2px}
.article p{margin:16px 0 0 4px;width:335px;font-size:8.4px;line-height:10.8px}
.more{color:var(--orange);font-size:8.4px;display:block;margin:4px 0 0 4px;text-decoration:none}
.owners{position:absolute;left:63px;top:545px;width:104px;height:100px;background:var(--pale);border:1px solid #f0c98a;color:var(--grey);font-size:8px;display:flex;align-items:center;justify-content:center}
.experts-text{position:absolute;left:186px;top:547px;width:210px;font-size:8.4px;line-height:10.8px}

/* sidebar */
.side-head{position:absolute;left:523px;width:284px;height:30px;border-radius:14px 14px 0 0;font-family:"Cinzel",serif;font-size:9.5px;text-align:center;padding-top:7px;color:#3a2a10}
.side-head.warm{background:linear-gradient(180deg,#fbb82b,#fed58a)}
.side-head.cool{background:linear-gradient(180deg,#c9e6f7,#eef7fc)}
.side-body{position:absolute;left:523px;width:284px;background:var(--white);border-radius:14px 14px 0 0}
.photo{position:absolute}
.cat{position:absolute;left:634px;width:172px;height:24px;border:1px solid #f5c77a;border-radius:12px 12px 0 0;background:linear-gradient(180deg,#fff9ee,#fde9c3);font-size:8.5px;padding:6px 0 0 22px}
.cat.hl{color:var(--link-blue)}
.cat.blue{background:linear-gradient(180deg,#e4f3fc,#cfe9f8);border-color:#a9d6f0}
.tags{left:560px;top:419px;width:210px;text-align:center;font-size:8.5px;line-height:11px}
.tags span{margin:0 4px}
.story{left:636px;top:642px;width:160px;font-size:8.4px;line-height:10.5px}
.story b{font-weight:400;color:var(--gold)}
.post{position:absolute;left:534px;width:263px;border-bottom:1px solid #ddd;padding-bottom:6px}
.post .icon{position:absolute;left:0;top:2px;width:22px;height:22px;border-radius:50%;background:#fbe2a0;border:1px solid #f5c77a}
.post .news-box{position:absolute;left:0;top:4px;width:22px;height:22px;border:1px solid #bbb}
.post p{margin-left:29px;font-size:8.4px;line-height:10.6px}
.post b{font-weight:400;color:var(--gold)}
.post .more{display:inline;margin:0 0 0 4px}

/* footer */
.footer{left:88px;top:1060px;width:723px;height:108px;background:var(--orange);overflow:hidden}
.fcol{position:absolute;top:10px;font-size:7.6px;line-height:8px}
.fcol h3{font-family:"Cinzel",serif;font-weight:400;font-size:8.5px;color:var(--red);margin-bottom:6px}
.fcol a{display:block;color:var(--ink);text-decoration:none}
.fcol a.hover{color:var(--magenta)}
.fcol a.visited{color:#d98a4a}
.copyright{left:340px;top:1176px;font-size:7.5px;display:flex;align-items:center;gap:5px}
.copyright i{display:block;width:10px;height:10px;border-radius:50%;background:var(--orange-deep)}
</style>
</head>
<body>

<div class="banner" style="left:88px;top:12px;width:351px;height:45px">BANNER</div>
<div class="banner" style="left:460px;top:12px;width:351px;height:45px">BANNER</div>

<header class="masthead abs">
  <div class="masthead-photo abs" role="img" aria-label="Photo of an active woman in a sun hat enjoying the sunshine"></div>
  <div class="brand abs"><i></i>Velvet Larks</div>
  <p class="tagline abs">Dangerously Fascinating Women</p>
  <p class="strapline abs">everything on our site is based<br>on personal experiences,<br>opinion and interpretation.</p>
</header>

<nav class="topnav abs">
  <span class="home-tab abs"></span>
  <a class="current" style="left:13px">home</a>
  <a style="left:88px">about us</a>
  <a style="left:164px">blog</a>
  <a class="contact" style="left:221px">contact (link colour on mouse over it)</a>
  <a class="search-label" style="left:488px">search</a>
  <span class="search-box"></span>
  <a class="search-label" style="left:648px">RSS Feed</a>
  <svg class="rss" viewBox="0 0 20 20"><circle cx="4" cy="16" r="2.6" fill="#f7a81b"/><path d="M2 9a9 9 0 0 1 9 9" stroke="#f7a81b" stroke-width="2.6" fill="none"/><path d="M2 3a15 15 0 0 1 15 15" stroke="#f7a81b" stroke-width="2.6" fill="none"/></svg>
</nav>

<div class="tabs abs">
  <div class="tab active" style="left:5px">What is HRT?
    <svg width="22" height="22" viewBox="0 0 22 22"><circle cx="11" cy="11" r="10" fill="none" stroke="#fff" stroke-width="1.5"/><circle cx="11" cy="11" r="6" fill="none" stroke="#fff" stroke-width="1.5"/><circle cx="11" cy="11" r="2.5" fill="#fff"/></svg>
  </div>
  <div class="tab" style="left:148px">Suffering<br>from migraines?</div>
  <div class="tab" style="left:292px">Do symptoms<br>get worse when you<br>start on HRT?</div>
  <div class="tab" style="left:435px">Treatment Options</div>
  <div class="tab" style="left:578px">Boost your sex drive</div>
</div>

<div class="main abs"></div>

<main class="content abs">
  <section class="article" style="top:35px">
    <h2>What is "the Menopause"</h2>
    <p>This is an ever-evolving site. We will be adding more information and stories over the coming months. Tell us what you want to see and read about using the feedback questionnaire! This is an ever-evolving site. We will be adding more information and stories over the coming months. Tell us what you want to see and read about using the feedback questionnaire! This is an ever-evolving site. We will be adding more information and stories over the coming months. Tell us what you want to see and read about using the feedback questionnaire! This is an ever-evolving site. We will be adding more information and stories over the coming months. Tell us what you want to see and read about using the feedback questionnaire! This is an ever-evolving site. We will be adding more information and stories over the coming months. Tell us what you want to see and read about using the feedback questionnaire!</p>
    <a class="more" href="#">read more...</a>
  </section>
  <section class="article" style="top:229px">
    <h2>HRT - Hormone Replacement Treatment</h2>
    <p>We haven't got all the answers but one thing we do know is that it helps to have friends - friends that you can honestly talk to about how you feel and what you are going through. We haven't got all the answers but one thing we do know is that it helps to have friends - friends that you can honestly talk to about how you feel and what you are going through. We haven't got all the answers but one thing we do know is that it helps to have friends - friends that you can honestly talk to about how you feel and what you are going through.</p>
    <a class="more" href="#">read more...</a>
  </section>
  <section class="article" style="top:369px">
    <h2>Relationships</h2>
    <p>We know we can't take the place of your friends and we don't want to – friends are a vital part of our lives. What we do offer is a place to read about things that are important to you, share experiences, discover possibilities. We know we can't take the place of your friends and we don't want to – friends are a vital part of our lives. What we do offer is a place to read about things that are important to you, share experiences, discover possibilities. We know we can't take the place of your friends and we don't want to – friends are a vital part of our lives.</p>
    <a class="more" href="#">read more...</a>
  </section>
  <section class="article" style="top:509px">
    <h2>Ask our Experts</h2>
  </section>
  <div class="owners" role="img" aria-label="Photo of the site owners">pic of owners</div>
  <div class="experts-text">There are some issues/problems which, for one reason or another, just can't be shared with friends or family. We offer an alternative - somewhere non-judgemental to share problems and get impartial opinions. There are some issues/problems which, for one reason or another, just can't be shared with friends or family. We offer an alternative - somewhere non-judgemental to share problems and get impartial opinions. We offer an alternative - somewhere non-judgemental to share problems and get impartial opinions.
    <a class="more" href="#" style="margin-left:0">read more...</a>
  </div>
</main>

<aside>
  <div class="side-head warm" style="top:280px">Blog Categories</div>
  <div class="side-body" style="top:304px;height:95px"></div>
  <div class="photo" role="img" aria-label="Photo of a smiling couple with a surfboard on the beach" style="left:532px;top:313px;width:89px;height:73px;background:linear-gradient(135deg,#9fc6e0,#e9d2b8 55%,#c89c74)"></div>
  <div class="cat" style="top:305px">explore something new</div>
  <div class="cat hl" style="top:328px">health &amp; well being</div>
  <div class="cat" style="top:351px">relationships</div>
  <div class="cat blue" style="top:374px">mind, body &amp; soul</div>

  <div class="tags abs">Room for tag cloud<br><span>Menopause</span><span>Hormones</span><span>Mid Life</span><span>Stress</span><br><span>Womans Health</span><span>HRT</span><span>Body &amp; Soul</span><br><span>hormone replacement therapy</span><span>Empty Nest</span></div>

  <div class="banner" style="left:534px;top:493px;width:126px;height:95px">BANNER</div>
  <div class="banner" style="left:669px;top:493px;width:126px;height:95px">BANNER</div>

  <div class="side-head warm" style="top:602px">Your Stories</div>
  <div class="side-body" style="top:626px;height:68px"></div>
  <div class="photo" role="img" aria-label="Photo of a woman in flowing white fabric against the sky" style="left:532px;top:636px;width:89px;height:48px;background:linear-gradient(180deg,#6fa6d4,#cfe3f1 60%,#f3f3f3)"></div>
  <div class="story abs"><b>I did it!</b><br>I don't quite know how it happened or why I chose the new craft I did really...<br><a class="more" href="#" style="text-align:right;margin:0">read more...</a></div>

  <div class="side-head cool" style="top:700px">Recent Blog Posts</div>
  <div class="side-body" style="top:724px;height:107px"></div>
  <div class="post" style="top:731px"><span class="icon"></span><p><b>Blogger's Nic:</b> Trying to understand the whole hormone/menopause thing? <a class="more" href="#">read more...</a></p></div>
  <div class="post" style="top:766px"><span class="icon"></span><p><b>Blogger's Nic:</b> This icon will be shown when blogger has no her own avatar <a class="more" href="#">read more...</a></p></div>
  <div class="post" style="top:802px;border:none"><span class="icon"></span><p><b>Blogger's Nic:</b> This icon will be shown when blogger has no her own avatar <a class="more" href="#">read more...</a></p></div>

  <div class="banner" style="left:534px;top:845px;width:261px;height:45px">BANNER</div>

  <div class="side-head cool" style="top:902px">Company News</div>
  <div class="side-body" style="top:926px;height:128px"></div>
  <div class="post" style="top:934px"><span class="news-box"></span><p><b>News head shot</b> Company news. Just some words in two lines <a class="more" href="#">read more...</a></p></div>
  <div class="post" style="top:969px"><span class="news-box"></span><p><b>News head shot</b> Company news. Just some words in two lines <a class="more" href="#">read more...</a></p></div>
  <div class="post" style="top:1005px"><span class="news-box"></span><p><b>News head shot</b> Company news. Just some words in two lines <a class="more" href="#">read more...</a></p></div>
</aside>

<footer class="footer abs">
  <div class="fcol" style="left:43px"><h3>See our blog archives</h3>
    <a href="#">Link to the category topic</a><a href="#">Link to the category topic</a><a href="#">Link to the category topic</a><a href="#">Link to the category topic</a><a href="#">Link to the category topic</a><a href="#">Link to the category topic</a></div>
  <div class="fcol" style="left:312px"><h3>Like to contact us</h3>
    <a href="mailto:info@velvetlarks.com">info@velvetlarks.com</a><a href="#">Link to the category topic</a><a href="#">Link to the category topic</a><a href="#">Link to the category topic</a><a href="#">Link to the category topic</a><a href="#">Link to the category topic</a></div>
  <div class="fcol" style="left:567px"><h3>Send us your stories...</h3>
    <a class="hover" href="#">Link when mous over it</a><a href="#">Link to the category topic</a><a class="visited" href="#">Visited link to the category topic</a><a href="#">Link to the category topic</a><a href="#">Link to the category topic</a><a href="#">Link to the category topic</a></div>
</footer>

<div class="copyright abs"><i></i>© VelvetLarks.com</div>

</body>
</html>
```